Zielgruppe
Der Honig soll in 35g Gläschen als kleines Gastgeschenk ausgegeben und darüber hinaus an im privaten Umfeld in 250g Gläsern verkauft werden.
Corporate Identity des Betriebes ist nicht zu beachten, da dies mein persönliches Hobby ist
Aufgabenstellung
Der Name des Honigs : BRUNTALERA
"gewonnen auf dem Dach Köln Altstadt"
Alle auf dem Etikett vorgeschrieben Angaben wie Menge (250g ; 35g), Name/Adresse des Imkers
Mindestens Haltbar bis + Leerfeld/Platz um Datum einzustempeln...gerne auch kreative Lösung um Stempel zu vermeiden
"Ursprungsland: Deutschland" oder "Deutscher Honig"
"Vor Licht und Wärme geschützt lagern"
Es werden Etiketten für zwei Füllmengen (250g und 35g Probierglas) benötigt.
Desweiteren werden für die 250g Gläser Gewähretiketten benötigt die sich am Etikettendesign orientieren und die Sorte angeben - Sommerhonig / Sommerblüte
Alternativ kann die Sorte auch auf dem Etikett angegeben werden
Ergänzung:
Etikettengröße für 250g Höhe max. 4cm x Breite max 10cm
Etikettengröße Probierglas Höhe max 2cm x Breite 8-10cm

```html
<!DOCTYPE html>
<html lang="de">
<head>
<meta charset="utf-8">
<title>BRUNTALERA – Sommerhonig 250g Etikett</title>
<link rel="stylesheet" href="https://fonts.googleapis.com/css2?family=Barlow+Semi+Condensed:wght@300;400&family=Pacifico&display=swap">
<style>
  :root {
    --paper: #ffffff;
    --ink: #111111;
    --gold: #e0bc5e;
    --comb: #f3e7c4;
  }
  html, body {
    margin: 0;
    padding: 0;
    overflow: hidden;
    background: var(--paper);
  }
  .label {
    position: relative;
    width: 1200px;
    height: 480px;
    overflow: hidden;
    background: var(--paper);
    font-family: "Barlow Semi Condensed", "Arial Narrow", sans-serif;
    color: var(--ink);
  }
  .comb-field {
    position: absolute;
    background: radial-gradient(ellipse at center, var(--comb) 0%, rgba(243,231,196,0.45) 55%, rgba(255,255,255,0) 80%);
  }
  .comb-field--left { left: -60px; top: 180px; width: 470px; height: 330px; }
  .comb-field--center { left: 360px; top: 300px; width: 240px; height: 200px; }
  .comb-field--right { left: 600px; top: -40px; width: 640px; height: 440px; }

  .vertical {
    position: absolute;
    writing-mode: vertical-rl;
    white-space: nowrap;
    font-weight: 300;
    line-height: 1;
  }
  .origin { left: 158px; top: 48px; font-size: 29px; font-weight: 400; }
  .beekeeper { left: 109px; top: 48px; font-size: 27px; }
  .address { left: 78px; top: 48px; font-size: 27px; }
  .phone { left: 48px; top: 48px; font-size: 27px; }

  .vertical--up { transform: rotate(180deg); }
  .storage { left: 965px; bottom: 34px; font-size: 27px; }
  .best-before { left: 1006px; bottom: 34px; font-size: 27px; font-weight: 400; }

  .brand {
    position: absolute;
    left: 0;
    width: 1200px;
    top: 108px;
    text-align: center;
    font-size: 62px;
    font-weight: 400;
    line-height: 52px;
    letter-spacing: 1px;
  }
  .origin-line {
    position: absolute;
    left: 0;
    width: 1200px;
    top: 304px;
    text-align: center;
    font-size: 32px;
    font-weight: 300;
    line-height: 35px;
    letter-spacing: 0.5px;
  }
  .weight {
    position: absolute;
    left: 312px;
    top: 392px;
    font-size: 42px;
    font-weight: 300;
    line-height: 1;
  }
  .variety {
    position: absolute;
    left: 452px;
    top: 372px;
    font-family: "Pacifico", cursive;
    font-size: 40px;
    line-height: 1.2;
    color: var(--gold);
  }
</style>
</head>
<body>
  <div class="label">
    <div class="comb-field comb-field--left" role="img" aria-label="Dezentes Wabenmuster in hellem Honiggelb"></div>
    <div class="comb-field comb-field--center" role="img" aria-label="Dezentes Wabenmuster in hellem Honiggelb"></div>
    <div class="comb-field comb-field--right" role="img" aria-label="Dezentes Wabenmuster in hellem Honiggelb"></div>

    <div class="vertical origin">DEUTSCHER HONIG</div>
    <div class="vertical beekeeper">Michael Vossler</div>
    <div class="vertical address">Lindenweg 14 | 51143 Köln</div>
    <div class="vertical phone">0151 4820917</div>

    <h1 class="brand" style="margin:0">BRUN<br>TALERA</h1>

    <p class="origin-line" style="margin:0">gewonnen auf dem Dach<br>des Lindenhof Köln Altstadt</p>

    <div class="weight">250g</div>
    <div class="variety">Sommerhonig</div>

    <div class="vertical vertical--up storage">Vor Licht und Wärme geschützt lagern</div>
    <div class="vertical vertical--up best-before">mindestens haltbar bis</div>
  </div>
</body>
</html>
```